Home Page Design

We are refreshing our website and need someone to design a very clean modern home page. We have a wireframe for the content and basic layout (see attached). We just need someone to make it look beautiful.

This web page will be hosted on a private server using HTML5. I have developers who will integrate the rotating images and referenced video files - we just need you to focus on the visual elements.

You can take a look at our current website at tavenfold.com for color style guides, logos, etc.

```html
<!DOCTYPE html>
<html lang="en">
<head>
<meta charset="utf-8">
<title>Tavenfold — Nimbus Cost Optimization</title>
<link href="https://fonts.googleapis.com/css2?family=Lato:wght@400;700;900&display=swap" rel="stylesheet">
<style>
:root{
  --blue:#2b9fdb;
  --blue-deep:#1f7fd6;
  --blue-light:#3fb1ee;
  --ink:#333a40;
  --muted:#555c63;
  --topbar:#3b3d40;
  --gray-bg:#f1f2f4;
  --footer:#2e3033;
  --footer-deep:#232427;
  --white:#ffffff;
}
*{box-sizing:border-box;margin:0;padding:0}
html,body{width:1200px;height:3622px;overflow:hidden}
body{position:relative;font-family:'Lato',sans-serif;color:var(--ink);background:var(--white)}
.abs{position:absolute}
.btn{position:absolute;display:flex;align-items:center;justify-content:center;background:var(--blue);color:#fff;font-weight:900;font-size:14px;letter-spacing:.5px;border-radius:22px;text-transform:uppercase}
.topbar{left:0;top:0;width:1200px;height:60px;background:var(--topbar);color:#e6e6e6;font-size:13px}
.topbar .links{position:absolute;left:75px;top:22px;display:flex;gap:16px}
.topbar .links span.sep{color:#999}
.topbar .phone{position:absolute;right:75px;top:21px;display:flex;align-items:center;gap:8px}
.header{left:0;top:60px;width:1200px;height:121px;background:#fff}
.brand{position:absolute;left:75px;top:30px;display:flex;align-items:center;gap:10px;font-size:36px;font-weight:700;color:var(--blue)}
.brand i{width:30px;height:30px;border-radius:50%;background:var(--blue);display:block}
.nav{position:absolute;left:492px;top:47px;display:flex;gap:40px;font-size:13px;font-weight:700;color:#222}
.hero{left:0;top:181px;width:1200px;height:592px;background:linear-gradient(120deg,#1d2f43 0%,#4f6d86 40%,#7d98ad 60%,#2d3e52 100%)}
.hero h1{position:absolute;left:75px;top:190px;color:#fff;font-size:38px;font-weight:900;line-height:47px}
.hero .tagline{position:absolute;left:75px;top:475px;color:#fff;font-size:13px;font-weight:700;display:flex;gap:9px}
.badge{position:absolute;width:300px;height:170px}
.badge svg{position:absolute;left:0;top:0}
.badge .txt{position:absolute;left:0;top:12px;width:300px;height:150px;display:flex;flex-direction:column;align-items:center;justify-content:center;color:#fff;text-align:center}
.badge .small{font-size:17px;font-weight:700;line-height:20px}
.badge .big{font-size:54px;font-weight:900;line-height:54px}
.edge{position:absolute;left:0;width:1200px;height:90px}
.sec-gray{left:0;top:1300px;width:1200px;height:500px;background:var(--gray-bg)}
.sec-blue{left:0;top:2290px;width:1200px;height:560px;background:linear-gradient(180deg,var(--blue-light),var(--blue-deep))}
.footer{left:0;top:3330px;width:1200px;height:292px;background:var(--footer)}
h2{position:absolute;font-size:29px;font-weight:700;color:#3a4046;letter-spacing:.5px;text-transform:uppercase}
.checks{position:absolute;list-style:none;font-size:14.5px;color:var(--muted);line-height:20px}
.checks li{position:relative;padding-left:30px;margin-bottom:9px}
.checks li::before{content:"";position:absolute;left:0;top:3px;width:15px;height:15px;border-radius:50%;background:var(--blue)}
.checks li::after{content:"";position:absolute;left:5px;top:6px;width:4px;height:7px;border:solid #fff;border-width:0 2px 2px 0;transform:rotate(45deg)}
.photo{position:absolute;border-radius:6px}
.arrow{position:absolute;width:14px;height:14px;border:solid #555;border-width:0 2px 2px 0}
.quote-head{left:599px;top:2402px;width:526px;text-align:center;color:#fff;font-size:17px;font-weight:700}
.stars{left:799px;top:2432px;display:flex;gap:4px}
.testimonial{left:75px;top:2532px;width:470px;color:#fff;font-size:14px;line-height:25px}
.sig{left:75px;top:2678px;color:#fff;font-size:14px;line-height:22px}
.assess-sub{left:75px;top:3012px;color:var(--blue);font-size:18px;font-weight:700}
.assess-body{left:75px;top:3044px;width:490px;color:var(--muted);font-size:14.5px;line-height:25px}
.fcol{position:absolute;top:3418px;font-size:13px;color:#ddd;line-height:25px}
.fcol h4{color:var(--blue);font-size:13px;font-weight:900;margin-bottom:4px;text-transform:uppercase}
.social{left:869px;top:3418px}
.social .row{display:flex;gap:16px;margin-top:14px}
.social .row i{width:24px;height:24px;border-radius:50%;background:#e8e8e8;display:block}
.bottombar{left:0;top:3572px;width:1200px;height:50px;background:var(--footer-deep);color:#ccc;font-size:12px}
.bottombar .copy{position:absolute;left:75px;top:19px}
.bottombar .legal{position:absolute;right:75px;top:19px;display:flex;gap:8px}
</style>
</head>
<body>

<div class="abs topbar">
  <div class="links"><span>About Us</span><span class="sep">|</span><span>Contact</span><span class="sep">|</span><span>Support</span><span class="sep">|</span><span>Partners</span></div>
  <div class="phone">
    <svg width="12" height="12" viewBox="0 0 24 24"><path fill="#e6e6e6" d="M6.6 10.8a15 15 0 0 0 6.6 6.6l2.2-2.2a1 1 0 0 1 1-.25 11.4 11.4 0 0 0 3.6.57 1 1 0 0 1 1 1V20a1 1 0 0 1-1 1A17 17 0 0 1 3 4a1 1 0 0 1 1-1h3.5a1 1 0 0 1 1 1c0 1.250.2 2.450.57 3.570a1 1 0 0 1-.25 1z"/></svg>
    <span>+1 (800) 555-0142</span>
  </div>
</div>

<div class="abs header">
  <div class="brand"><i></i>tavenfold</div>
  <div class="nav"><span>SOLUTIONS</span><span>PRICING</span><span>FAQ</span></div>
  <div class="btn" style="left:862px;top:38px;width:166px;height:40px;font-size:12px">Free Assesment</div>
  <div class="btn" style="left:1035px;top:38px;width:90px;height:40px;font-size:12px">Log In</div>
</div>

<div class="abs hero" role="img" aria-label="Photo of hands typing on a laptop with cost and analytics doodles floating above">
  <h1>The Ultimate Nimbus<br>Cost Optimization Solutions</h1>
  <div class="btn" style="left:75px;top:318px;width:165px;height:38px">What We Do</div>
  <div class="tagline"><span>Next Gen Technology</span><span>|</span><span>Advanced Cost Analytics</span><span>|</span><span>Managed Services</span><span>|</span><span>Certified Nimbus Engineers</span></div>

  <div class="badge" style="left:825px;top:120px">
    <svg width="300" height="170" viewBox="0 0 300 170"><g fill="var(--blue)" stroke="#fff" stroke-width="4" paint-order="stroke"><ellipse cx="150" cy="95" rx="140" ry="62"/><circle cx="110" cy="45" r="36"/><circle cx="180" cy="38" r="40"/><circle cx="245" cy="68" r="34"/></g><g fill="var(--blue)"><ellipse cx="150" cy="95" rx="138" ry="60"/><circle cx="110" cy="45" r="34"/><circle cx="180" cy="38" r="38"/><circle cx="245" cy="68" r="32"/></g></svg>
    <div class="txt"><span class="small">Average Reduction</span><span class="big">47%</span><span class="small">Total Nimbus Spend</span></div>
  </div>
  <div class="badge" style="left:825px;top:305px">
    <svg width="300" height="170" viewBox="0 0 300 170"><g fill="var(--blue)" stroke="#fff" stroke-width="4" paint-order="stroke"><ellipse cx="150" cy="95" rx="140" ry="62"/><circle cx="110" cy="45" r="36"/><circle cx="180" cy="38" r="40"/><circle cx="245" cy="68" r="34"/></g><g fill="var(--blue)"><ellipse cx="150" cy="95" rx="138" ry="60"/><circle cx="110" cy="45" r="34"/><circle cx="180" cy="38" r="38"/><circle cx="245" cy="68" r="32"/></g></svg>
    <div class="txt"><span class="small">Average Cash ROI</span><span class="big">5.1x</span><span class="small">First Year</span></div>
  </div>
</div>

<svg class="edge" style="top:700px" viewBox="0 0 1200 90"><g fill="#fff"><circle cx="40" cy="110" r="70"/><circle cx="160" cy="100" r="60"/><circle cx="280" cy="115" r="75"/><circle cx="420" cy="100" r="65"/><circle cx="560" cy="112" r="72"/><circle cx="700" cy="95" r="60"/><circle cx="830" cy="110" r="70"/><circle cx="960" cy="100" r="62"/><circle cx="1080" cy="112" r="70"/><circle cx="1190" cy="100" r="60"/><rect x="0" y="70" width="1200" height="20"/></g></svg>

<!-- NextGen technology -->
<div class="photo" style="left:113px;top:842px;width:437px;height:350px;background:linear-gradient(180deg,#3a3d42 0%,#d9e1e7 40%,#c4ced6 75%,#2a2c30 100%)" role="img" aria-label="Photo of a monitor showing the optimization scheduling dashboard"></div>
<div class="arrow" style="left:80px;top:978px;transform:rotate(135deg)"></div>
<div class="arrow" style="left:568px;top:978px;transform:rotate(-45deg)"></div>

<h2 style="left:647px;top:838px">NextGen Technology</h2>
<ul class="checks" style="left:647px;top:893px">
  <li>Extensive library of proprietary optimization tools.</li>
  <li>NBS volume rightsizing.</li>
  <li>Computesize optimization.</li>
  <li>Advanced scheduling.</li>
  <li>Identify and manage orphaned resources.</li>
  <li>Retain complete control over your environment.</li>
  <li>Schedule and automate optimization actions.</li>
  <li>Extensive value tracking and reporting.</li>
</ul>
<div class="btn" style="left:649px;top:1153px;width:166px;height:38px">Read More</div>

<svg class="edge" style="top:1212px" viewBox="0 0 1200 90"><g fill="var(--gray-bg)"><circle cx="60" cy="110" r="60"/><circle cx="190" cy="115" r="70"/><circle cx="330" cy="100" r="60"/><circle cx="470" cy="112" r="70"/><circle cx="610" cy="98" r="58"/><circle cx="740" cy="112" r="70"/><circle cx="880" cy="100" r="62"/><circle cx="1010" cy="112" r="72"/><circle cx="1150" cy="102" r="65"/><rect x="0" y="75" width="1200" height="15"/></g></svg>

<div class="abs sec-gray"></div>
<h2 style="left:75px;top:1366px">Advanced Cost Analytics</h2>
<ul class="checks" style="left:75px;top:1421px">
  <li>Extensive library of proprietary optimization tools.</li>
  <li>NBS volume rightsizing.</li>
  <li>Computesize optimization.</li>
  <li>Advanced scheduling.</li>
  <li>Identify and manage orphaned resources.</li>
  <li>Retain complete control over your environment.</li>
  <li>Schedule and automate optimization actions.</li>
  <li>Extensive value tracking and reporting.</li>
</ul>
<div class="btn" style="left:77px;top:1682px;width:166px;height:38px">Read More</div>
<div class="photo" style="left:599px;top:1371px;width:526px;height:348px;background:linear-gradient(135deg,#c9d3dc,#7a8b9c 55%,#2a3440)" role="img" aria-label="Photo of business people reviewing charts on a tablet"></div>

<svg class="edge" style="top:1720px" viewBox="0 0 1200 90"><g fill="#fff"><circle cx="30" cy="115" r="70"/><circle cx="170" cy="100" r="60"/><circle cx="300" cy="112" r="70"/><circle cx="440" cy="98" r="60"/><circle cx="580" cy="112" r="72"/><circle cx="720" cy="100" r="60"/><circle cx="860" cy="115" r="75"/><circle cx="1000" cy="100" r="62"/><circle cx="1130" cy="110" r="70"/><rect x="0" y="75" width="1200" height="15"/></g></svg>

<!-- Managed services -->
<div class="photo" style="left:75px;top:1890px;width:526px;height:348px;background:linear-gradient(135deg,#5a3f2e,#2b2420 60%,#1a1a1a)" role="img" aria-label="Photo of hands holding a tablet with glowing cloud service icons"></div>
<h2 style="left:647px;top:1886px">Managed Services</h2>
<ul class="checks" style="left:647px;top:1941px;width:465px">
  <li>Outsource cost optimization to the experts Customized solutions that fit your environment Dedicated team of Certified Nimbus Engineers and financial analysts.</li>
  <li>Continuous monitoring of your Nimbus environment.</li>
  <li>Deep analysis of Nimbus usage data and billing activity Regular meetings to review trends, anomalies and cost saving opportunities.</li>
  <li>Detailed analysis of your monthly invoice with comprehensive variance analysis.</li>
</ul>
<div class="btn" style="left:649px;top:2200px;width:166px;height:38px">Read More</div>

<!-- customers -->
<div class="abs sec-blue"></div>
<svg class="edge" style="top:2272px" viewBox="0 0 1200 90"><g fill="#fff"><circle cx="50" cy="-10" r="55"/><circle cx="180" cy="0" r="50"/><circle cx="320" cy="-15" r="60"/><circle cx="470" cy="0" r="48"/><circle cx="610" cy="-12" r="60"/><circle cx="760" cy="0" r="50"/><circle cx="900" cy="-15" r="60"/><circle cx="1040" cy="0" r="50"/><circle cx="1170" cy="-10" r="55"/></g></svg>
<div class="abs quote-head">"Using Tavenfold is a No Brainer"</div>
<div class="abs stars">
  <svg width="125" height="24" viewBox="0 0 125 24"><g fill="#ffd21f"><path id="st" d="M12 1l3.3 7 7.7.9-5.7 5.2 1.5 7.6L12 18l-6.8 3.7 1.5-7.6L1 8.9l7.7-.9z"/><use href="#st" x="25"/><use href="#st" x="50"/><use href="#st" x="75"/><use href="#st" x="100"/></g></svg>
</div>
<h2 style="left:75px;top:2476px;color:#fff">Listen to Our Customers</h2>
<p class="abs testimonial">" Lorem ipsum dolor sit amet, consectetur adipiscing elit. Vestibulum sed turpis libero. Integer elit nisi, pellentesque id diam sodales, tristique commodo sapien. Fusce vitae vestibulum metus, quis facilisis neque curabitur sagittis ut urna ac consectetur. In ullamcorper lorem lacus. Donec id felis nec ligula dignissim lobortis..."</p>
<div class="abs sig"><b>-NAME HEADING</b><br>Cloud Engeering</div>
<div class="photo" style="left:599px;top:2472px;width:526px;height:261px;background:linear-gradient(120deg,#e8edf1,#b9c4cc 50%,#4a5866)" role="img" aria-label="Photo of a smiling businessman working on a laptop in an office"></div>
<svg class="edge" style="top:2780px" viewBox="0 0 1200 90"><g fill="#fff"><circle cx="40" cy="110" r="70"/><circle cx="180" cy="100" r="62"/><circle cx="320" cy="115" r="72"/><circle cx="460" cy="98" r="60"/><circle cx="600" cy="112" r="70"/><circle cx="740" cy="100" r="62"/><circle cx="880" cy="115" r="72"/><circle cx="1020" cy="98" r="60"/><circle cx="1160" cy="110" r="70"/><rect x="0" y="70" width="1200" height="20"/></g></svg>

<!-- free assessment -->
<h2 style="left:75px;top:2964px">Free Assessment</h2>
<div class="abs assess-sub">No Risk ● Real Cost Savings Estimate</div>
<p class="abs assess-body">Wondering if Tavenfold a good fit for your organization?<br>Take the guess work out of it and sign for a free assessment. Our team of cloud analysts will work with you to perform of reassessment of your Nimbus enviornment, including the specific cost saving opportunites they identified and the potential annual savings.</p>
<div class="btn" style="left:77px;top:3207px;width:166px;height:38px">Free Assesment</div>
<div class="photo" style="left:599px;top:2926px;width:526px;height:347px;background:linear-gradient(135deg,#7d8d9c,#3a4a5c 55%,#1e2a38)" role="img" aria-label="Photo of a businessman touching a virtual screen labelled Assessment"></div>

<!-- footer -->
<div class="abs footer"></div>
<svg class="edge" style="top:3250px" viewBox="0 0 1200 90"><g fill="var(--footer)"><circle cx="60" cy="110" r="65"/><circle cx="200" cy="100" r="60"/><circle cx="340" cy="115" r="72"/><circle cx="480" cy="98" r="58"/><circle cx="620" cy="112" r="70"/><circle cx="760" cy="100" r="62"/><circle cx="900" cy="115" r="72"/><circle cx="1040" cy="100" r="60"/><circle cx="1170" cy="110" r="68"/><rect x="0" y="80" width="1200" height="10"/></g></svg>
<div class="fcol" style="left:75px"><h4>Company</h4>About Us<br>Contact Us</div>
<div class="fcol" style="left:266px"><h4>Product</h4>Solutions<br>Features<br>Pricing<br>FAQ</div>
<div class="fcol" style="left:444px"><h4>Customers</h4>Sales<br>Supports</div>
<div class="fcol" style="left:647px"><h4>Partners</h4>Become a Rsellers<br>Portal Login</div>
<div class="fcol social"><h4>Follow Us</h4><div class="row"><i></i><i></i><i></i><i></i><i></i></div></div>
<div class="abs bottombar">
  <div class="copy">Copyright © 2019. Tavenfold.All Rights Reserved.</div>
  <div class="legal"><span>Privacy Policy</span><span>|</span><span>Terms of Services</span></div>
</div>

</body>
</html>
```